A postcard needed for a kids gym

We are a kids gym opening soon. We are called Bouncewell Kids Gym. Here is the website so that you can get more details on what it is we will be doing. www.Bouncewellkidsgym.example I am including a screen shot of wallpaper we are using on two walls that will be prominently displayed in our building. I was wondering if the wall paper can somehow be included in the postcard as a soft background or something?no postage or mail info needed as this will be passed out by hand. I am also sending our logo and colors. Thank you for your help, and we look forward to hearing and seeing what you have to present. Sincerely,Lorraine

Target Market(s)

Parents

Industry/Entity Type

Childcare

Requirements
Must have
• "Opening soon"

```html
<!DOCTYPE html>
<html lang="en">
<head>
<meta charset="utf-8">
<title>Bouncewell Kids Gym – Opening Soon</title>
<link rel="stylesheet" href="https://fonts.googleapis.com/css2?family=Quicksand:wght@300;400;700&display=swap">
<style>
  :root {
    --sky-blue: #26a8e0;
    --mist-white: #f3f4f3;
    --mist-grey: #e8eae8;
    --trunk-grey: #dcdfdc;
    --floor-grey: #e4e6e4;
  }
  * { margin: 0; padding: 0; box-sizing: border-box; }
  html, body {
    width: 1200px;
    height: 929px;
    overflow: hidden;
    background: var(--mist-white);
  }
  .postcard {
    position: relative;
    width: 1200px;
    height: 929px;
    overflow: hidden;
    font-family: "Quicksand", sans-serif;
    color: var(--sky-blue);
    text-align: center;
  }
  .wallpaper-backdrop {
    position: absolute;
    inset: 0;
    background:
      linear-gradient(180deg, rgba(243,244,243,0) 0%, rgba(243,244,243,0) 70%, var(--floor-grey) 100%),
      linear-gradient(90deg,
        var(--mist-grey) 0%, var(--mist-white) 10%, var(--trunk-grey) 20%,
        var(--mist-white) 32%, var(--mist-grey) 44%, var(--trunk-grey) 54%,
        var(--mist-white) 66%, var(--mist-grey) 78%, var(--mist-white) 88%, var(--trunk-grey) 100%);
  }
  .brand-name {
    position: absolute;
    top: 140px;
    left: 0;
    width: 100%;
    font-weight: 700;
    font-size: 84px;
    line-height: 1;
    letter-spacing: -1px;
  }
  .headline {
    position: absolute;
    top: 368px;
    left: 0;
    width: 100%;
    font-weight: 700;
    font-size: 116px;
    line-height: 1;
    letter-spacing: -1px;
  }
  .contact {
    position: absolute;
    top: 630px;
    left: 0;
    width: 100%;
    font-weight: 300;
    font-size: 56px;
    line-height: 73px;
    font-style: normal;
  }
</style>
</head>
<body>
  <main class="postcard">
    <div class="wallpaper-backdrop" role="img" aria-label="Soft, faded wallpaper photo of a misty forest with tall tree trunks"></div>
    <h1 class="brand-name">Bouncewell Kids Gym</h1>
    <p class="headline">opening soon</p>
    <address class="contact">
      www.Bouncewellkidsgym.example<br>
      482 Maple Grove Avenue<br>
      Fairview, CA 90000
    </address>
  </main>
</body>
</html>
```